Updating Company Website with New Brand Collateral

Needing to update the current website to the new company name and brand.
Square Space platform

A home landing page with an additional secure blog site.

Current website at: https://www.quillbrookco.com/

Once the basic design and flow it set up, I will add content in after the fact.

Like Website like:
https://www.kowelgrp.com/
https://www.xmfhospitality.com/
https://www.vorlenddentalservices.com/

Industry/Entity Type

Small Business

Coding

Coded - Design and coding required

Number of Pages Required

5+ page

Font styles to use
Sans Serif

Requirements
Must have
• Clear, clean design that is easy to navigate.
Home page
About us
Locations
Blog/News
Contact us
Join our team
Nice to have
• Interactive Map of locations

```html
<!DOCTYPE html>
<html lang="en">
<head>
<meta charset="utf-8">
<title>Norvale — Real Estate and Development</title>
<link href="https://fonts.googleapis.com/css2?family=Poppins:wght@400;500;600;700&family=Open+Sans:wght@400;600&display=swap" rel="stylesheet">
<style>
:root{
  --teal:#1c9bb0;
  --teal-deep:#0c78a3;
  --teal-soft:#4fb6c4;
  --ink:#1b1b1b;
  --body:#5a5a5a;
  --muted:#8a8a8a;
  --band:#ececec;
  --white:#ffffff;
  --line:#dcdcdc;
}
*{box-sizing:border-box;margin:0;padding:0}
html,body{width:1200px;height:4092px;overflow:hidden}
body{position:relative;background:var(--white);font-family:"Open Sans",Arial,sans-serif;color:var(--body)}
.abs{position:absolute}
h1,h2,h3,h4,.brand,.nav a,.btn{font-family:"Poppins",Arial,sans-serif}
.section-title{position:absolute;left:0;width:1200px;text-align:center;font-size:34px;font-weight:700;color:var(--ink);letter-spacing:.5px}
.btn{position:absolute;display:inline-block;border-radius:22px;background:var(--teal);color:var(--white);font-size:13px;font-weight:600;text-transform:uppercase;text-align:center;letter-spacing:.5px;text-decoration:none}

/* header / hero */
.hero-photo{left:0;top:0;width:1200px;height:780px;background:linear-gradient(100deg,#f1f3f3 0%,#e6eaea 45%,#d9dfdf 70%,#cfd6d6 100%)}
.hero-object{left:660px;top:120px;width:340px;height:560px;border-radius:60px 60px 70px 70px;background:radial-gradient(ellipse at 55% 22%,#6fb13a 0%,#4c8f2a 22%,rgba(160,120,70,.85) 50%,#8a6a45 72%,rgba(210,215,215,0) 100%)}
.brand{left:110px;top:40px;display:flex;align-items:center;gap:12px;font-size:40px;font-weight:700;color:var(--ink)}
.brand .mark{width:26px;height:26px;background:var(--teal)}
.nav{left:388px;top:50px;display:flex}
.nav a{display:block;padding:0 22px;height:36px;line-height:36px;font-size:13px;font-weight:500;color:var(--ink);text-decoration:none;text-transform:uppercase;border-right:1px solid var(--line)}
.nav a:last-child{border-right:none}
.nav a.current{color:var(--teal);border-bottom:3px solid var(--teal)}
.hero-title{left:110px;top:262px;width:460px;font-size:41px;line-height:50px;font-weight:700;color:var(--ink)}
.hero-text{left:110px;top:420px;width:440px;font-size:15px;line-height:22px;color:var(--body)}
.hero .btn{left:110px;top:500px;width:150px;height:44px;line-height:44px}
.slider-dots{left:1130px;top:330px;display:flex;flex-direction:column;gap:14px}
.slider-dots span{width:12px;height:12px;border-radius:50%;border:2px solid #9aa;background:transparent}
.slider-dots span.on{background:#9aa}
.hero-wave{left:0;top:660px}

/* about */
.about-photo{left:110px;top:830px;width:450px;height:400px;background:linear-gradient(135deg,#7fa86a 0%,#b79c6c 45%,#9a8466 70%,#d8cdb8 100%)}
.about-accent{left:60px;top:940px;width:100px;height:180px;border-radius:0 90px 90px 0;background:var(--teal)}
.about-title{left:600px;top:828px;font-size:40px;font-weight:700;color:var(--ink)}
.about-text{left:600px;width:490px;font-size:15px;line-height:22px}
.about .btn{left:600px;top:1180px;width:160px;height:46px;line-height:46px}

/* services */
.services{left:0;top:1330px;width:1200px;height:540px;background:var(--band)}
.service-card{top:1468px;width:236px;height:310px;overflow:hidden}
.service-card .photo{position:absolute;inset:0}
.service-card .shade{position:absolute;inset:0;background:linear-gradient(180deg,rgba(0,0,0,.05) 0%,rgba(0,0,0,.45) 100%)}
.service-card h3{position:absolute;left:0;right:0;top:168px;text-align:center;font-size:20px;line-height:25px;font-weight:600;color:var(--white)}
.service-card .more{position:absolute;left:0;right:0;top:258px;text-align:center;font-family:"Poppins",Arial,sans-serif;font-size:11px;font-weight:600;color:var(--white)}
.service-card .bar{position:absolute;left:0;bottom:0;width:100%;height:8px;background:var(--teal)}
.slide-arrow{top:1596px;width:40px;height:40px}

/* blog */
.blog-band{left:0;top:1870px}
.blog-card{top:1992px;width:312px;height:338px;background:var(--white);overflow:hidden}
.blog-card .photo{height:205px}
.blog-card h3{padding:22px 22px 0;font-size:20px;line-height:25px;font-weight:600;color:var(--ink)}
.blog-card .date{padding:12px 22px 0;font-size:11px;font-weight:600;color:var(--teal);text-transform:uppercase;display:flex;align-items:center;gap:8px}
.blog-more{left:490px;top:2370px;width:220px;height:50px;line-height:50px;background:var(--white);color:var(--ink);border-radius:25px}

/* team */
.member{top:2680px;width:220px;text-align:center}
.member .avatar{width:190px;height:190px;margin:0 auto;border-radius:50%;border:6px solid #e6e6e6}
.member h4{margin-top:18px;font-size:20px;font-weight:700;color:var(--ink)}
.member .rule{width:190px;height:3px;margin:10px auto 0;background:var(--teal)}
.member .role{margin-top:14px;font-family:"Poppins",Arial,sans-serif;font-size:13px;font-weight:600;color:var(--ink)}
.member p{margin:12px auto 0;width:180px;font-size:12px;line-height:17px;color:var(--muted)}

/* contact */
.contact{left:0;top:3120px;width:1200px;height:560px;background:var(--band)}
.map{left:110px;top:3200px;width:455px;height:340px;background:linear-gradient(160deg,#e4e8d8 0%,#d9e3cf 40%,#cfdbe0 75%,#d6dee2 100%)}
.map-note{left:140px;top:3226px;width:210px;padding:10px 12px;background:var(--white);font-size:11px;line-height:15px;box-shadow:0 2px 6px rgba(0,0,0,.15)}
.contact-title{left:720px;top:3195px;font-size:36px;font-weight:700;color:var(--ink)}
.contact-item{left:720px;display:flex;gap:18px;align-items:flex-start}
.contact-item .icon{width:48px;height:48px;border-radius:50%;background:var(--teal);display:flex;align-items:center;justify-content:center;flex:none}
.contact-item strong{display:block;font-family:"Poppins",Arial,sans-serif;font-size:13px;color:var(--ink)}
.contact-item span{display:block;font-size:12px;line-height:17px;color:var(--body)}

/* footer */
.footer-band{left:0;top:3620px}
.social{left:110px;top:3782px;display:flex;gap:14px}
.social span{width:16px;height:16px;border-radius:50%;background:var(--white);opacity:.9}
.footer-rule{left:110px;top:3818px;width:50px;height:2px;background:var(--white)}
.footer-links{left:110px;top:3840px;list-style:none;font-size:13px;line-height:22px;color:var(--white)}
.footer-heading{font-family:"Poppins",Arial,sans-serif;font-size:21px;font-weight:500;color:var(--white)}
.newsletter-text{left:460px;top:3810px;width:280px;text-align:center;font-size:12px;line-height:17px;color:#e4f4f6}
.newsletter-field{left:470px;top:3862px;width:270px;height:40px;border:1px solid var(--white);padding:0 14px;line-height:38px;font-size:13px;color:var(--white)}
.newsletter-btn{left:470px;top:3920px;width:270px;height:40px;line-height:40px;background:var(--teal-soft);color:var(--white);border-radius:0;font-size:12px}
.footer-about{left:850px;top:3810px;width:240px;text-align:right;font-size:12px;line-height:17px;color:#e4f4f6}
.copyright{left:0;top:4030px;width:1200px;text-align:center;font-size:13px;color:var(--white)}
.copyright-rule{left:0;top:4005px;width:1200px;height:1px;background:rgba(255,255,255,.25)}
</style>
</head>
<body>

<!-- Hero -->
<section class="hero">
  <div class="abs hero-photo" role="img" aria-label="Bright blurred office background"></div>
  <div class="abs hero-object" role="img" aria-label="Glass jar full of coins with a young green plant growing from it"></div>
  <div class="abs brand"><span class="mark"></span>Norvale</div>
  <nav class="abs nav">
    <a class="current" href="#">Home</a>
    <a href="#">About us</a>
    <a href="#">Locations</a>
    <a href="#">Blog/News</a>
    <a href="#">Contact us</a>
    <a href="#">Join the team</a>
  </nav>
  <h1 class="abs hero-title">WE SPECIALISE IN REALESTATE AND DEVLOPEMENT</h1>
  <p class="abs hero-text">We plan, build and manage homes and workspaces across the region, with care for every owner we serve.</p>
  <a class="btn" href="#">Get started</a>
  <div class="abs slider-dots"><span class="on"></span><span></span><span></span></div>
  <svg class="abs hero-wave" width="1200" height="130" viewBox="0 0 1200 130">
    <polygon points="0,40 1200,95 1200,130 0,130" fill="#ffffff"/>
    <polygon points="0,20 700,80 0,118" fill="#1c9bb0"/>
    <polygon points="0,60 520,86 0,118" fill="#0c78a3"/>
    <polygon points="0,118 1200,96 1200,130 0,130" fill="#ffffff"/>
    <circle cx="600" cy="108" r="22" fill="#ffffff" stroke="#d8d8d8"/>
    <polyline points="592,104 600,112 608,104" fill="none" stroke="#555" stroke-width="2"/>
  </svg>
</section>

<!-- About -->
<section class="about">
  <div class="abs about-accent"></div>
  <div class="abs about-photo" role="img" aria-label="Hands holding stacked coins with small plants growing on top"></div>
  <h2 class="abs about-title">ABOUT NORVALE</h2>
  <p class="abs about-text" style="top:892px">Our team has guided owners, tenants and investors through every stage of property work for many years. We find good sites, shape clear plans, manage each build with care and keep every project on time, on budget and built to last for the people who live and work there.</p>
  <p class="abs about-text" style="top:1040px">From first talks to final handover, we stay close to our clients and the towns we work in. Each home, shop and office we deliver reflects honest advice, sound planning and long local roots, so every partner can move forward with real confidence.</p>
  <a class="btn" href="#">Contact us</a>
</section>

<!-- Services -->
<section>
  <div class="abs services"></div>
  <h2 class="section-title" style="top:1395px">OUR SERVICES</h2>
  <svg class="abs slide-arrow" style="left:0" viewBox="0 0 40 40"><circle cx="20" cy="20" r="20" fill="#1c9bb0"/><polyline points="23,13 16,20 23,27" fill="none" stroke="#fff" stroke-width="2.5"/></svg>
  <svg class="abs slide-arrow" style="left:1160px" viewBox="0 0 40 40"><circle cx="20" cy="20" r="20" fill="#1c9bb0"/><polyline points="17,13 24,20 17,27" fill="none" stroke="#fff" stroke-width="2.5"/></svg>

  <article class="abs service-card" style="left:108px">
    <div class="photo" role="img" aria-label="Business people shaking hands" style="background:linear-gradient(160deg,#8fa3b3,#b0b9c0 50%,#6e5e5a)"></div>
    <div class="shade"></div><h3>Lorem ipsum<br>dolor</h3><div class="more">LEARN MORE ›</div><div class="bar"></div>
  </article>
  <article class="abs service-card" style="left:356px">
    <div class="photo" role="img" aria-label="Small plant growing beside a stack of coins" style="background:linear-gradient(160deg,#c7d3cc,#9fb3a8 50%,#6d7f73)"></div>
    <div class="shade"></div><h3>Lorem ipsum<br>dolor</h3><div class="more">LEARN MORE ›</div><div class="bar"></div>
  </article>
  <article class="abs service-card" style="left:604px">
    <div class="photo" role="img" aria-label="Financial charts on a desk with a calculator" style="background:linear-gradient(160deg,#dfe3e6,#aab4bb 50%,#5d6a73)"></div>
    <div class="shade"></div><h3>Lorem ipsum<br>dolor</h3><div class="more">LEARN MORE ›</div><div class="bar"></div>
  </article>
  <article class="abs service-card" style="left:852px">
    <div class="photo" role="img" aria-label="Hands holding young seedlings in soil" style="background:linear-gradient(160deg,#6d9a95,#4c7f78 50%,#2f5a55)"></div>
    <div class="shade"></div><h3>Lorem ipsum<br>dolor</h3><div class="more">LEARN MORE ›</div><div class="bar"></div>
  </article>
</section>

<!-- Blog -->
<section>
  <svg class="abs blog-band" width="1200" height="680" viewBox="0 0 1200 680">
    <defs>
      <linearGradient id="blogGrad" x1="0" y1="0" x2="1" y2="1">
        <stop offset="0" stop-color="#3aa9b4"/>
        <stop offset="1" stop-color="#0c78a3"/>
      </linearGradient>
    </defs>
    <polygon points="0,0 1200,0 1200,590 0,660" fill="url(#blogGrad)"/>
    <polygon points="600,625 1200,590 1200,660" fill="#d0d0d0"/>
  </svg>
  <h2 class="section-title" style="top:1925px;color:#fff">OUR LATEST BLOG</h2>

  <article class="abs blog-card" style="left:108px">
    <div class="photo" role="img" aria-label="Team meeting around a table with laptops" style="background:linear-gradient(150deg,#2d3c4a,#6f7f8b 60%,#c7ccd0)"></div>
    <h3>Nemo enim ipsam volu ptatem quia</h3>
    <div class="date"><svg width="12" height="12" viewBox="0 0 12 12"><rect x="1" y="2" width="10" height="9" fill="none" stroke="#1c9bb0" stroke-width="1.5"/><line x1="1" y1="5" x2="11" y2="5" stroke="#1c9bb0" stroke-width="1.5"/></svg>Posted May 1, 2019</div>
  </article>
  <article class="abs blog-card" style="left:444px">
    <div class="photo" role="img" aria-label="People reviewing documents and charts on a desk" style="background:linear-gradient(150deg,#9aa8b4,#5f7282 60%,#dce2e6)"></div>
    <h3>Nemo enim ipsam volu ptatem quia</h3>
    <div class="date"><svg width="12" height="12" viewBox="0 0 12 12"><rect x="1" y="2" width="10" height="9" fill="none" stroke="#1c9bb0" stroke-width="1.5"/><line x1="1" y1="5" x2="11" y2="5" stroke="#1c9bb0" stroke-width="1.5"/></svg>Posted May 1, 2019</div>
  </article>
  <article class="abs blog-card" style="left:780px">
    <div class="photo" role="img" aria-label="Hands pointing at a printed business plan" style="background:linear-gradient(150deg,#e2e6e8,#b6c0c6 55%,#7e8c95)"></div>
    <h3>Nemo enim ipsam volu ptatem quia</h3>
    <div class="date"><svg width="12" height="12" viewBox="0 0 12 12"><rect x="1" y="2" width="10" height="9" fill="none" stroke="#1c9bb0" stroke-width="1.5"/><line x1="1" y1="5" x2="11" y2="5" stroke="#1c9bb0" stroke-width="1.5"/></svg>Posted May 1, 2019</div>
  </article>
  <a class="btn blog-more" href="#">View more blogs</a>
</section>

<!-- Team -->
<section>
  <h2 class="section-title" style="top:2600px">OUR TEAM</h2>
  <div class="abs member" style="left:122px">
    <div class="avatar" role="img" aria-label="Portrait of a team member" style="background:linear-gradient(180deg,#cfc9c4,#6b6f75)"></div>
    <h4>JOHN DOE</h4><div class="rule"></div><div class="role">COMPANY NAME</div>
    <p>Leads new projects and keeps every client in the loop.</p>
  </div>
  <div class="abs member" style="left:362px">
    <div class="avatar" role="img" aria-label="Portrait of a team member" style="background:linear-gradient(180deg,#d6d2cd,#5d636b)"></div>
    <h4>JOHN DOE</h4><div class="rule"></div><div class="role">COMPANY NAME</div>
    <p>Oversees site work, budgets and the build timeline.</p>
  </div>
  <div class="abs member" style="left:602px">
    <div class="avatar" role="img" aria-label="Portrait of a team member" style="background:linear-gradient(180deg,#d9d4cf,#4a4f57)"></div>
    <h4>JOHN DOE</h4><div class="rule"></div><div class="role">COMPANY NAME</div>
    <p>Handles leasing, tenants and care of our buildings.</p>
  </div>
  <div class="abs member" style="left:842px">
    <div class="avatar" role="img" aria-label="Portrait of a team member" style="background:linear-gradient(180deg,#d3cfca,#62666c)"></div>
    <h4>JOHN DOE</h4><div class="rule"></div><div class="role">COMPANY NAME</div>
    <p>Guides investors through each deal from start to end.</p>
  </div>
</section>

<!-- Contact -->
<section>
  <div class="abs contact"></div>
  <div class="abs map" role="img" aria-label="Map of office locations across the country"></div>
  <div class="abs map-note">24 Harbour Lane, Suite 3, Brookfield, open weekdays.</div>
  <svg class="abs" style="left:150px;top:3268px" width="18" height="24" viewBox="0 0 18 24"><path d="M9 0C4 0 0 4 0 9c0 7 9 15 9 15s9-8 9-15c0-5-4-9-9-9z" fill="#d9412e"/><circle cx="9" cy="9" r="3.5" fill="#fff"/></svg>
  <h2 class="abs contact-title">CONTACT US</h2>

  <div class="abs contact-item" style="top:3268px">
    <div class="icon"><svg width="18" height="22" viewBox="0 0 18 24"><path d="M9 0C4 0 0 4 0 9c0 7 9 15 9 15s9-8 9-15c0-5-4-9-9-9z" fill="#fff"/><circle cx="9" cy="9" r="3.5" fill="#1c9bb0"/></svg></div>
    <div><strong>Address :</strong><span>24 Harbour Lane, Suite 3<br>Brookfield, Ontario</span></div>
  </div>
  <div class="abs contact-item" style="top:3340px">
    <div class="icon"><svg width="20" height="20" viewBox="0 0 24 24"><path d="M6.6 10.8a15 15 0 006.6 6.6l2.2-2.2c.3-.3.7-.4 1-.2 1.1.4 2.3.6 3.6.6.6 0 1 .4 1 1V20c0 .6-.4 1-1 1C10.6 21 3 13.4 3 4c0-.6.4-1 1-1h3.5c.6 0 1 .4 1 1 0 1.300.2 2.5.6 3.6.1.3 0 .7-.2 1l-2.3 2.2z" fill="#fff"/></svg></div>
    <div><strong>Phone :</strong><span>(555) 010-2468</span></div>
  </div>
  <div class="abs contact-item" style="top:3412px">
    <div class="icon"><svg width="22" height="16" viewBox="0 0 22 16"><rect x="1" y="1" width="20" height="14" fill="none" stroke="#fff" stroke-width="2"/><polyline points="1,1 11,9 21,1" fill="none" stroke="#fff" stroke-width="2"/></svg></div>
    <div><strong>Mail us :</strong><span>info@norvale.com</span></div>
  </div>
  <div class="abs contact-item" style="top:3484px">
    <div class="icon"><svg width="22" height="22" viewBox="0 0 22 22"><circle cx="11" cy="11" r="9" fill="none" stroke="#fff" stroke-width="2"/><ellipse cx="11" cy="11" rx="4" ry="9" fill="none" stroke="#fff" stroke-width="1.5"/><line x1="2" y1="11" x2="20" y2="11" stroke="#fff" stroke-width="1.5"/></svg></div>
    <div><strong>Website :</strong><span>www.norvale.com</span></div>
  </div>
</section>

<!-- Footer -->
<footer>
  <svg class="abs footer-band" width="1200" height="472" viewBox="0 0 1200 472">
    <defs>
      <linearGradient id="footGrad" x1="0" y1="0" x2="1" y2="1">
        <stop offset="0" stop-color="#2aa2b2"/>
        <stop offset="1" stop-color="#0c78a3"/>
      </linearGradient>
    </defs>
    <polygon points="0,0 700,60 1200,40 1200,472 0,472" fill="url(#footGrad)"/>
    <polygon points="0,0 700,60 0,80" fill="#4fb6c4"/>
  </svg>
  <div class="abs social"><span></span><span></span><span></span><span></span><span></span></div>
  <div class="abs footer-rule"></div>
  <ul class="abs footer-links">
    <li>Home</li><li>About us</li><li>Locations</li><li>Blog/News</li><li>Contact Us</li><li>Join the Team</li>
  </ul>
  <h3 class="abs footer-heading" style="left:460px;top:3765px;width:280px;text-align:center">Norvale Newsletter</h3>
  <p class="abs newsletter-text">Sign up to get project news, market notes and fresh listings.</p>
  <div class="abs newsletter-field">Email address</div>
  <div class="btn newsletter-btn">Subscribe</div>
  <h3 class="abs footer-heading" style="left:850px;top:3765px;width:240px;text-align:right">About Norvale</h3>
  <p class="abs footer-about">We are a local property team building homes, shops and offices with honest advice, steady planning and lasting care for every town we serve.</p>
  <div class="abs copyright-rule"></div>
  <p class="abs copyright">© Copyright 2019 Norvale | All Rights Reserved</p>
</footer>

</body>
</html>
```